Chiropractic healthcare group business card

We are a Portland Oregon based chiropractic healthcare group. Looking for a new business card design. Something cutting edge, that shows off our new logo and tag line.Use either of the attached logos.Our tag line = "Who would you be without pain?"I'm open to about anything, impress me!!
Target Market(s)
Chiropractic patients - Auto injury, back pain, sports injuries, neck , shoulder, hip, knee, ankle pain.
Industry/Entity Type
Chiropractic
Contact Information for Business Card
Dr. Bram Holtvick, D.C.
Clinic name - Fernway Chiropractic
2 clinics
location #1
20418 NW Marwick Road
Suite B
North Plains, OR 97133
Location #2
13529 SE Calloway Street
Portland OR 97236
Main phone line 971.555.0143
website : www.FernwayClinics.example
Tag line "Who would you be without pain?"
Colors
Designer to choose colors to be used in the design.
Requirements
Must have
- Use the logo colors -- Want the orange color to be a TRUE orange.
- Both clinic address
- phone number
- website
- personal email - b.holtvick@ReliefBeginsHere.example
- tag line - "Who would you be without pain?"

```html
<!DOCTYPE html>
<html lang="en">
<head>
<meta charset="UTF-8">
<title>Fernway Chiropractic — Business Card Front</title>
<link rel="stylesheet" href="https://fonts.googleapis.com/css2?family=Arimo:ital,wght@0,400;0,700;1,400&display=swap">
<style>
  :root {
    --page-bg: #ffffff;
    --card-pattern-tone: #eeeeee;
    --card-border: #8a8a8a;
    --brand-orange: #f7941d;
    --brand-grey: #5f6062;
    --text-light: #ffffff;
  }
  * { margin: 0; padding: 0; box-sizing: border-box; }
  html, body {
    width: 1200px;
    height: 914px;
    overflow: hidden;
    background: var(--page-bg);
    font-family: "Arimo", Arial, sans-serif;
  }
  .sheet {
    position: relative;
    width: 1200px;
    height: 914px;
  }
  .card-front {
    position: absolute;
    left: 77px;
    top: 80px;
    width: 1044px;
    height: 652px;
    border: 1px solid var(--card-border);
    overflow: hidden;
  }
  .card-texture {
    position: absolute;
    inset: 0;
    background: linear-gradient(180deg, #f1f1f1 0%, var(--card-pattern-tone) 100%);
  }
  .brand-lockup {
    position: absolute;
    left: 0;
    right: 0;
    top: 264px;
    display: flex;
    justify-content: center;
    align-items: center;
    gap: 18px;
  }
  .brand-square {
    width: 34px;
    height: 34px;
    background: var(--brand-orange);
  }
  .brand-name {
    font-size: 50px;
    font-weight: 700;
    color: var(--brand-orange);
    letter-spacing: 0.5px;
  }
  .tagline-band {
    position: absolute;
    left: 230px;
    top: 433px;
    width: 584px;
    height: 56px;
  }
  .tagline-band svg {
    position: absolute;
    inset: 0;
  }
  .tagline-text {
    position: absolute;
    inset: 0;
    display: flex;
    align-items: center;
    justify-content: center;
    font-style: italic;
    font-weight: 400;
    font-size: 30px;
    letter-spacing: 1px;
    color: var(--text-light);
  }
  .side-label {
    position: absolute;
    right: 38px;
    top: 856px;
    font-size: 38px;
    font-weight: 700;
    color: var(--brand-grey);
  }
</style>
</head>
<body>
  <main class="sheet">
    <section class="card-front">
      <div class="card-texture" role="img" aria-label="Light grey repeating triangle pattern background"></div>

      <div class="brand-lockup">
        <span class="brand-square"></span>
        <span class="brand-name">Fernway Chiropractic</span>
      </div>

      <div class="tagline-band">
        <svg width="584" height="56" viewBox="0 0 584 56" aria-hidden="true">
          <polygon points="22,0 562,0 584,56 0,56" fill="var(--brand-grey)"/>
        </svg>
        <p class="tagline-text">Who would you be without pain?</p>
      </div>
    </section>

    <p class="side-label">Front</p>
  </main>
</body>
</html>
```